FUN and creative designs WANTED! Mobile Marketing Start-up Company

Website design needed.

- QB is a full service mobile marketing agency in existence to help connect companies with their audience on unwired devices (Smartphone and tablets).

- QB is a start-up business with no current website looking to make a solid, memorable first impression.
Updates

Please take into consideration the following two points from our brief:

-  sense of humour and fun. Showing that mobile marketing for your business can be easy, interesting, and not just for big companies.

- a little ‘left of centre’ (i.e. NOT corporate!)

Thanks!

Please don't use black as a back groud. 

Target Market(s)

Primarily Media Agencies and Direct clients of all business types

Industry/Entity Type

Marketing

Requirements
Must have
• •The website should be: simple, clean yet a little ‘left of centre’ (i.e. NOT corporate!)
•Colour-in-line with QB logo (Black, Grey and orange: RBG: 255, 59, 0)
•Font: Arial and Aller Bold as per logo
•The website needs to show the charter of the business- sense of humour and fun. Showing that mobile marketing for your business can be easy, interesting, and not just for big companies.

What pages are required:
-Home Page
-Why Mobile
-Why Quill
-Services
-Contact

* For initial submission only a home page and one sub-page is require as the other pages will work from the same template

* Coding would be great but not a essential
Nice to have
• Please suggest some stock photos for the website
Should not have
• Please review all attached documents:
* Full brief
* Logo files
* Web copy

```html
<!DOCTYPE html>
<html lang="en">
<head>
<meta charset="utf-8">
<title>Why Mobile – Quill Unwired</title>
<link rel="stylesheet" href="https://fonts.googleapis.com/css2?family=Signika:wght@600;700&family=Arimo:wght@400;700&display=swap">
<style>
  :root {
    --orange: #ff3b00;
    --ink: #1a1a1a;
    --text: #333333;
    --paper: #f8f6ef;
    --footer: #1c1c1c;
    --white: #ffffff;
    --mascot: #2a2a2a;
  }
  * { margin: 0; padding: 0; box-sizing: border-box; }
  html, body { width: 1200px; height: 1050px; overflow: hidden; }
  body {
    position: relative;
    background: var(--paper);
    font-family: "Arimo", Arial, sans-serif;
    color: var(--text);
  }
  .brand {
    position: absolute; left: 120px; top: 52px;
    display: flex; align-items: center; gap: 12px;
  }
  .brand-dot { width: 48px; height: 48px; border-radius: 50%; background: var(--orange); }
  .brand-name {
    font-family: "Signika", sans-serif; font-weight: 700;
    font-size: 46px; line-height: 1; color: #3a3a3a; letter-spacing: 1px;
  }
  .main-nav { position: absolute; top: 38px; left: 0; width: 1200px; height: 80px; }
  .main-nav a {
    position: absolute; top: 0; width: 140px; margin-left: -70px;
    display: flex; flex-direction: column; align-items: center;
    text-decoration: none; color: var(--ink);
    font-family: "Signika", sans-serif; font-weight: 600; font-size: 15px;
  }
  .main-nav a svg { height: 44px; width: 44px; margin-bottom: 14px; fill: var(--ink); }
  .main-nav a.is-current { color: var(--orange); }
  .page-title {
    position: absolute; left: 120px; top: 192px;
    font-family: "Signika", sans-serif; font-weight: 700;
    font-size: 37px; color: var(--orange);
  }
  .mascot { position: absolute; background: var(--mascot); border-radius: 40% 40% 45% 45%; }
  .mascot-phone { left: 632px; top: 168px; width: 96px; height: 76px; }
  .mascot-megaphone { left: 142px; top: 820px; width: 92px; height: 72px; }
  .copy { position: absolute; left: 120px; width: 615px; font-size: 14.5px; line-height: 21px; }
  .copy-first { top: 262px; }
  .copy-lead { top: 470px; color: var(--orange); font-size: 18px; line-height: 21px; }
  .copy-second { top: 535px; }
  .cta {
    position: absolute; left: 120px; top: 698px; width: 651px; height: 90px;
    background: var(--ink); color: var(--white);
    font-family: "Signika", sans-serif; font-weight: 600; font-size: 22px; line-height: 30px;
  }
  .cta-chevron { position: absolute; left: 230px; top: 0; width: 50px; height: 90px; }
  .cta-left { position: absolute; left: 15px; top: 12px; }
  .cta-right { position: absolute; left: 293px; top: 11px; }
  .cta-right em { font-style: normal; color: var(--orange); }
  .services { position: absolute; left: 783px; top: 221px; width: 260px; }
  .services h2 {
    font-family: "Signika", sans-serif; font-weight: 600;
    font-size: 20px; line-height: 23px; color: var(--ink); margin-bottom: 22px;
  }
  .services ul { list-style: none; }
  .services li {
    position: relative; padding-left: 29px; color: var(--orange);
    font-size: 14.5px; line-height: 15px; margin-bottom: 15px;
  }
  .services li svg { position: absolute; left: 0; top: -2px; width: 16px; height: 22px; fill: var(--ink); }
  .device {
    position: absolute; left: 816px; top: 505px; width: 166px; height: 325px;
    border-radius: 28px;
    background: linear-gradient(180deg, #2a2a2a 0%, #111 14%, #8aa071 40%, #c9b9a6 75%, #111 82%, #1a1a1a 100%);
  }
  .site-footer {
    position: absolute; left: 0; top: 894px; width: 1200px; height: 156px;
    background: var(--footer);
  }
  .footer-nav a {
    position: absolute; top: 24px; color: var(--orange); text-decoration: none;
    font-size: 13px; font-weight: 700; text-transform: uppercase;
  }
  .copyright { position: absolute; left: 121px; top: 62px; color: var(--white); font-size: 12px; }
  .social { position: absolute; right: 134px; top: 19px; display: flex; gap: 14px; }
  .social a {
    display: flex; align-items: center; gap: 5px;
    color: var(--orange); text-decoration: none; font-size: 12px; font-weight: 700;
  }
  .social a::before {
    content: ""; width: 24px; height: 24px; border-radius: 50%; background: var(--orange);
  }
</style>
</head>
<body>

<header>
  <div class="brand">
    <span class="brand-dot"></span>
    <span class="brand-name">quill</span>
  </div>

  <nav class="main-nav">
    <a href="#" style="left:455px">
      <svg viewBox="0 0 44 44"><path d="M22 6 L5 22 H10 V38 H19 V28 H25 V38 H34 V22 H39 Z"/></svg>
      HOME
    </a>
    <a href="#" class="is-current" style="left:587px">
      <svg viewBox="0 0 44 44"><rect x="13" y="8" width="18" height="34" rx="3"/><rect x="24" y="2" width="3" height="8"/><rect x="16" y="12" width="12" height="9" fill="#f8f6ef"/><g fill="#f8f6ef"><rect x="16" y="24" width="3" height="3"/><rect x="20.5" y="24" width="3" height="3"/><rect x="25" y="24" width="3" height="3"/><rect x="16" y="29" width="3" height="3"/><rect x="20.5" y="29" width="3" height="3"/><rect x="25" y="29" width="3" height="3"/><rect x="16" y="34" width="3" height="3"/><rect x="20.5" y="34" width="3" height="3"/><rect x="25" y="34" width="3" height="3"/></g></svg>
      WHY MOBILE
    </a>
    <a href="#" style="left:731px">
      <svg viewBox="0 0 44 44"><path d="M34 3 L14 22 H22 L8 41 L33 18 H24 Z"/></svg>
      WHY QUILL
    </a>
    <a href="#" style="left:861px">
      <svg viewBox="0 0 44 44"><circle cx="16" cy="16" r="9"/><circle cx="16" cy="16" r="3.5" fill="#f8f6ef"/><circle cx="30" cy="30" r="8"/><circle cx="30" cy="30" r="3" fill="#f8f6ef"/><g stroke="#1a1a1a" stroke-width="3"><path d="M16 4v24M4 16h24M7.5 7.5l17 17M24.5 7.5l-17 17"/><path d="M30 19v22M19 30h22M22.2 22.2l15.6 15.6M37.8 22.2L22.2 37.8"/></g><circle cx="16" cy="16" r="3.5" fill="#f8f6ef"/><circle cx="30" cy="30" r="3" fill="#f8f6ef"/></svg>
      SERVICES
    </a>
    <a href="#" style="left:998px">
      <svg viewBox="0 0 44 44"><rect x="15" y="2" width="14" height="26" rx="7"/><path d="M10 20 a12 12 0 0 0 24 0" fill="none" stroke="#1a1a1a" stroke-width="3"/><rect x="20.5" y="31" width="3" height="8"/><rect x="15" y="39" width="14" height="3"/></svg>
      CONTACT
    </a>
  </nav>
</header>

<main>
  <h1 class="page-title">Why Mobile</h1>
  <div class="mascot mascot-phone" role="img" aria-label="Cheeky cartoon mascot holding up a mobile phone"></div>

  <p class="copy copy-first">Lorem ipsum dolor sit amet, consectetur adipiscing elit. Donec rutrum blandit odio ac blandit. Phasellus vulputate nunc nec velit ultricies sed sagittis nisi convallis. Fusce mi justo, tempor a bibendum eu, dictum id metus. Suspendisse potenti. Mauris luctus, nulla eget rhoncus auctor, leo nunc dictum orci, eleifend feugiat quam tellus eu nunc. Vestibulum mollis neque in felis pellentesque rutrum. Maecenas tincidunt lectus sed nunc commodo facilisis. Donec sapien lorem, laoreet ac ornare et, pulvinar imperdiet tortor. Mauris sollicitudin tincidunt lorem, ac imperdiet lorem posuere id. Nunc vitae tellus in tellus fermentum rutrum sed pretium velit. Phasellus eget tellus sed dui suscipit aliquam et in lorem. Vivamus vitae leo at tellus commodo tincidunt.</p>

  <p class="copy copy-lead">Lorem ipsum dolor sit amet, consectetur adipiscing elit. Maecenas sollicitudin augue et orci vulputate accumsan.</p>

  <p class="copy copy-second">Aliquam pulvinar varius leo id rutrum. Cras dictum lorem non leo fringilla a fringilla ipsum egestas. Donec nec ante odio, et venenatis nulla. Etiam suscipit, augue eu eleifend feugiat, enim urna facilisis felis, adipiscing pellentesque justo nisi sed magna. Pellentesque nunc augue, molestie eget accumsan quis, sodales sed metus. In molestie ullamcorper mauris ut cursus. Proin nec massa sit amet libero ultricies posuere eget quis sem. Quisque mi sapien, malesuada a ultrices sit amet, ornare sed orci. Nullam volutpat nisi ac tellus pharetra fermentum.</p>

  <section class="cta">
    <p class="cta-left">Unleash your mobile<br>potential now</p>
    <svg class="cta-chevron" viewBox="0 0 50 90"><path d="M0 0 H22 L50 45 L22 90 H0 L28 45 Z" fill="#ff3b00"/></svg>
    <p class="cta-right">Get Quill Unwired on <em>XXXXXXXX</em><br>or email <em>XXXXXXXXXXXXXXXX</em></p>
  </section>

  <div class="mascot mascot-megaphone" role="img" aria-label="Cartoon mascot shouting through a megaphone"></div>

  <aside class="services">
    <h2>Quill Unwired<br>services include:</h2>
    <ul>
      <li><svg viewBox="0 0 16 22"><path d="M15 0 L5 10 H9 L1 22 L14 8 H9 Z"/></svg>Mobile Strategy/consultancy</li>
      <li><svg viewBox="0 0 16 22"><path d="M15 0 L5 10 H9 L1 22 L14 8 H9 Z"/></svg>Mobile training and research</li>
      <li><svg viewBox="0 0 16 22"><path d="M15 0 L5 10 H9 L1 22 L14 8 H9 Z"/></svg>Full management, optimization, reporting and insights</li>
      <li><svg viewBox="0 0 16 22"><path d="M15 0 L5 10 H9 L1 22 L14 8 H9 Z"/></svg>Creative development and production</li>
      <li><svg viewBox="0 0 16 22"><path d="M15 0 L5 10 H9 L1 22 L14 8 H9 Z"/></svg>Mobile brand building/brand development</li>
    </ul>
  </aside>

  <div class="device" role="img" aria-label="Smartphone showing a 'Why Quill? More customers, spending more money, more often' screen with a photo of hands holding a phone"></div>
</main>

<footer class="site-footer">
  <nav class="footer-nav">
    <a href="#" style="left:120px">Home</a>
    <a href="#" style="left:191px">Why Mobile</a>
    <a href="#" style="left:304px">Why Quill</a>
    <a href="#" style="left:397px">Services</a>
    <a href="#" style="left:500px">Contact</a>
  </nav>
  <p class="copyright">Copyright 2012 Quill Unwired. All rights reserved.</p>
  <div class="social">
    <a href="#">Linkline</a>
    <a href="#">Chirpr</a>
    <a href="#">Friendbook</a>
  </div>
</footer>

</body>
</html>
```